MLD Illustration Web Design

Create illustration web design company for Mandirasa Luhur Digital (MLD). I more prefer design with illustration concept. Detail for requirement please see attach file. I'm also attach MLD logo. This logo had 2 type, 2D design and 3D design. You can chose one of them, or used both.
For the winner or had good design would be possible to private project to completeness this website
Attach file requirement is guidance for design, but any changes are welcome
Updates
Sorry, I forgot about contact. Please add menu contact. You can put this menu besides login menu or part of menu level #1, or put on some where to adjust your design. Menu contact will give pop up window to email MLD Company and Company Information (Address, Telephone, etc)
Target Market(s)
Company (Business To Business)
Industry/Entity Type
It Company
Look and feel
Each slider illustrates characteristics of the customer's brand and the style your logo design should communicate.

```html
<!DOCTYPE html>
<html lang="en">
<head>
<meta charset="utf-8">
<title>MLD — Mandirasa Luhur Digital</title>
<link href="https://fonts.googleapis.com/css2?family=Arimo:wght@400;700&display=swap" rel="stylesheet">
<style>
  :root{
    --sky-top:#0b2a63;
    --sky-mid:#2f66b0;
    --sky-low:#a9cfea;
    --snow:#eef3f7;
    --band:#10223f;
    --navy:#12244a;
    --nav-text:#d8e4f4;
    --accent:#1f8fe0;
    --login:#0b5fa8;
    --green-top:#8dc63f;
    --green-bot:#3d7a12;
    --body-text:#5a6a82;
    --logo-green:#9ccc2e;
    --pill-top:#ffffff;
    --pill-bot:#d9dde2;
  }
  *{box-sizing:border-box;margin:0;padding:0}
  html,body{width:1200px;height:1000px;overflow:hidden;background:var(--band)}
  body{font-family:"Arimo",Arial,sans-serif;position:relative}
  .hero{position:absolute;left:0;top:0;width:1200px;height:788px;
    background:linear-gradient(180deg,var(--sky-top) 0%,var(--sky-mid) 30%,var(--sky-low) 58%,#f4f8fb 70%,var(--snow) 100%)}
  .cloud-art{position:absolute;left:260px;top:95px;width:720px;height:560px;
    background:radial-gradient(ellipse 45% 50% at 50% 45%,rgba(255,255,255,.95) 0%,rgba(255,255,255,.75) 45%,rgba(255,255,255,0) 75%);}
  .devices-art{position:absolute;left:462px;top:605px;width:245px;height:115px;
    background:linear-gradient(135deg,#9aa7b5,#2e4a6e 55%,#dfe6ec);border-radius:6px;opacity:.9}
  .logo{position:absolute;left:20px;top:14px;display:flex;align-items:center;gap:10px}
  .logo-dot{width:50px;height:50px;border-radius:50%;background:var(--logo-green)}
  .logo-name{font-weight:700;font-size:46px;color:var(--logo-green);letter-spacing:2px}
  .nav{position:absolute;top:30px;left:462px;display:flex;align-items:center}
  .nav a{color:var(--nav-text);font-size:12px;font-weight:700;text-decoration:none;padding:0 18px;height:30px;line-height:30px;border-left:1px solid #b9c9de}
  .nav a:first-child{border-left:none}
  .nav a.active{color:#fff;box-shadow:inset 0 -4px 0 var(--accent);line-height:30px}
  .nav a.login{border:none;background:linear-gradient(#1a78c8,var(--login));color:#cfe6ff;width:78px;text-align:center;padding:0;margin-left:16px;height:32px}
  .pill{position:absolute;height:26px;border-radius:13px;background:linear-gradient(var(--pill-top),var(--pill-bot));
    box-shadow:2px 3px 4px rgba(0,0,0,.3);color:#2b3442;font-size:15px;line-height:26px;text-align:center}
  .icon{position:absolute}
  .welcome{position:absolute;left:406px;top:811px;width:92px;height:34px;border-radius:5px;
    background:linear-gradient(var(--green-top),var(--green-bot));color:#fff;font-weight:700;font-size:16px;line-height:34px;text-align:center;box-shadow:2px 3px 4px rgba(0,0,0,.5)}
  .col{position:absolute;top:858px;width:215px;font-size:9px;line-height:12px;color:var(--body-text);text-align:justify}
  .more{position:absolute;top:957px;width:78px;height:18px;background:var(--accent);color:#fff;font-size:8px;line-height:18px;text-align:center;border-radius:2px}
  .subscribe-field{position:absolute;left:896px;top:972px;width:208px;height:17px;background:#4a4f57;color:#cfd5dd;font-size:8px;line-height:17px;padding-left:24px}
  .subscribe-btn{position:absolute;left:1115px;top:972px;width:66px;height:17px;background:var(--accent);color:#fff;font-size:8px;line-height:17px;text-align:center}
</style>
</head>
<body>
  <div class="hero" role="img" aria-label="Snowy landscape under a blue sky"></div>
  <div class="cloud-art" role="img" aria-label="Swirling white cloud with glowing blue light orbs"></div>
  <div class="devices-art" role="img" aria-label="Monitor, tablet and phone resting in the snow"></div>

  <div class="logo"><span class="logo-dot"></span><span class="logo-name">MLD</span></div>

  <nav class="nav">
    <a class="active">HOME</a><a>SERVICES</a><a>PRODUCT</a><a>CLIENTS</a><a>COMPANY</a><a>BLOG</a><a>CONTACT</a><a class="login">LOGIN</a>
  </nav>

  <div class="pill" style="left:548px;top:166px;width:85px">Services</div>
  <div class="pill" style="left:509px;top:245px;width:84px">Product</div>
  <div class="pill" style="left:487px;top:325px;width:84px">Clients</div>
  <div class="pill" style="left:476px;top:403px;width:82px">Company</div>
  <div class="pill" style="left:475px;top:482px;width:84px">Blog</div>

  <svg class="icon" style="left:660px;top:155px" width="44" height="50" viewBox="0 0 44 50"><path d="M3 3h28l10 10v34H3z" fill="none" stroke="var(--navy)" stroke-width="4"/><path d="M11 18h22M11 25h22M11 32h22M11 39h22" stroke="var(--navy)" stroke-width="3"/></svg>
  <svg class="icon" style="left:620px;top:234px" width="42" height="48" viewBox="0 0 42 48"><path d="M21 2 40 12 21 22 2 12z" fill="var(--navy)"/><path d="M2 15 19 24v22L2 36z" fill="var(--navy)"/><path d="M40 15 23 24v22l17-10z" fill="var(--navy)"/></svg>
  <svg class="icon" style="left:599px;top:304px" width="40" height="50" viewBox="0 0 40 50"><circle cx="20" cy="11" r="10" fill="var(--navy)"/><path d="M2 48c0-16 6-24 18-24s18 8 18 24z" fill="var(--navy)"/><path d="M20 26l3 6-3 12-3-12z" fill="#fff"/></svg>
  <svg class="icon" style="left:585px;top:390px" width="46" height="46" viewBox="0 0 46 46"><circle cx="23" cy="23" r="20" fill="none" stroke="var(--navy)" stroke-width="5"/></svg>
  <svg class="icon" style="left:585px;top:467px" width="48" height="48" viewBox="0 0 48 48"><circle cx="14" cy="34" r="9" fill="none" stroke="var(--navy)" stroke-width="6"/><path d="M5 6v28" stroke="var(--navy)" stroke-width="6"/><path d="M18 16a18 18 0 0 1 14 14M22 6a26 26 0 0 1 22 22" fill="none" stroke="var(--navy)" stroke-width="6"/></svg>
  <svg class="icon" style="left:589px;top:552px" width="22" height="40" viewBox="0 0 22 40"><path d="M0 0h22L11 40z" fill="var(--navy)"/></svg>

  <div class="welcome">Welcome!</div>
  <p class="col" style="left:406px">Lorem ipsum badama dolor sit amet, consectetur adipisicing elit, sed do eiusmod tempor incididunt ut labore et dolore magna aliqua. Ut enim ad minim veniam, quis nostrud exercitation ullamco laboris nisi ut aliquip ex ea commodo consequat. Duis aute irure dolor in reprehenderit in voluptate velit esse cillum dolore eu.</p>
  <p class="col" style="left:632px">Lorem ipsum badama dolor sit amet, consectetur adipisicing elit, sed do eiusmod tempor incididunt ut labore et dolore magna aliqua. Ut enim ad minim veniam, quis nostrud exercitation ullamco laboris nisi ut aliquip ex ea commodo consequat. Duis aute irure dolor in reprehenderit in voluptate velit esse cillum dolore eu.</p>
  <div class="more" style="left:406px">LEARN MORE</div>
  <div class="more" style="left:632px">LEARN MORE</div>

  <div class="subscribe-field">your email address...</div>
  <svg class="icon" style="left:903px;top:976px" width="12" height="9" viewBox="0 0 12 9"><rect x=".5" y=".5" width="11" height="8" fill="none" stroke="#e6ebf0"/><path d="M.5 .5 6 5l5.5-4.5" fill="none" stroke="#e6ebf0"/></svg>
  <div class="subscribe-btn">SUBSCRIBE</div>
</body>
</html>
```